Financial Planning Firm needs a client data collection summary sheet to print on A3

We are a financial advice company, and we are after a 1-page sheet where we can write all of the client’s personal information in our meetings, like a mind map.
It should have our logo on the page along with a place to put the Client's Name and the Date.
It also needs to have the following Headings
Family
Home
Investments
Business
Estate Plan
Lifestyle
Money
Retirement
Dreams & Goals
Health and Wellbeing
It also needs to have our License details on the bottom: Tellora Counsel Pty Ltd (538216) is an Authorised Representative of Brindle Estate Capital Group Pty Ltd AFSL No: 613985 ABN 57 218 964 402. This document has been prepared by Tellora Counsel and is for general information only.
Please utilise our colour scheme as per our logo attached. Please find uploaded to the project an example data collection summary sheet that we use currently.

```html
<!DOCTYPE html>
<html lang="en">
<head>
<meta charset="utf-8">
<title>Client Mind Map – Tellora Counsel</title>
<link rel="stylesheet" href="https://fonts.googleapis.com/css2?family=Arimo:wght@400&display=swap">
<style>
  :root {
    --page-bg: #b3b3b3;
    --sheet: #ffffff;
    --band: #05080a;
    --ink: #111111;
    --band-text: #ffffff;
    --rule: #555555;
  }
  html, body {
    margin: 0;
    width: 1200px;
    height: 1200px;
    overflow: hidden;
    background: var(--page-bg);
    font-family: "Arimo", Arial, sans-serif;
  }
  .sheet {
    position: absolute;
    left: 0;
    top: 175px;
    width: 1200px;
    height: 850px;
    background: var(--sheet);
  }
  .sheet svg { display: block; width: 100%; height: 100%; }
  .brand-band { fill: var(--band); }
  .brand-name { fill: var(--band-text); font-size: 38px; letter-spacing: 5px; text-anchor: middle; }
  .field-label { fill: var(--ink); font-size: 10px; }
  .field-line { stroke: var(--rule); stroke-width: 1; stroke-dasharray: 3 2; }
  .branch { fill: none; stroke: var(--ink); stroke-width: 2; }
  .hub { fill: var(--sheet); stroke: var(--ink); stroke-width: 2; }
  .hub-text { fill: var(--ink); font-size: 46px; text-anchor: middle; }
  .topic { fill: var(--ink); font-size: 25px; }
  .topic-right { text-anchor: end; }
  .icon { fill: none; stroke: var(--ink); stroke-width: 1.8; stroke-linecap: round; stroke-linejoin: round; }
  .icon-text { fill: var(--ink); font-size: 20px; text-anchor: middle; }
  .licence { fill: var(--ink); font-size: 18.5px; text-anchor: middle; }
</style>
</head>
<body>
<div class="sheet">
<svg viewBox="0 0 1378 976" xmlns="http://www.w3.org/2000/svg">
  <!-- Header -->
  <rect class="brand-band" x="0" y="0" width="1378" height="130"/>
  <text class="brand-name" x="689" y="78">TELLORA COUNSEL</text>

  <!-- Client fields -->
  <text class="field-label" x="60" y="171">Name</text>
  <line class="field-line" x1="94" y1="171" x2="366" y2="171"/>
  <text class="field-label" x="479" y="171">Date</text>
  <line class="field-line" x1="505" y1="171" x2="658" y2="171"/>
  <line class="field-line" x1="60" y1="225" x2="668" y2="225"/>

  <!-- Branches -->
  <polyline class="branch" points="142,332 467,332 645,509"/>
  <polyline class="branch" points="142,449 519,449 617,545"/>
  <polyline class="branch" points="142,571 613,571"/>
  <polyline class="branch" points="142,694 519,694 617,597"/>
  <polyline class="branch" points="142,811 467,811 645,633"/>
  <polyline class="branch" points="1235,332 909,332 732,509"/>
  <polyline class="branch" points="1235,449 857,449 760,545"/>
  <polyline class="branch" points="1235,571 763,571"/>
  <polyline class="branch" points="1235,694 857,694 760,597"/>
  <polyline class="branch" points="1235,811 909,811 732,633"/>

  <!-- Hub -->
  <circle class="hub" cx="688" cy="571" r="75"/>
  <text class="hub-text" x="688" y="567">MIND</text>
  <text class="hub-text" x="688" y="608">MAP</text>

  <!-- Left topics -->
  <text class="topic" x="157" y="320">Family</text>
  <text class="topic" x="157" y="439">Home</text>
  <text class="topic" x="157" y="562">Investments</text>
  <text class="topic" x="157" y="681">Business</text>
  <text class="topic" x="157" y="795">Estate Plan</text>

  <!-- Right topics -->
  <text class="topic topic-right" x="1222" y="316">Lifestyle</text>
  <text class="topic topic-right" x="1222" y="437">Money</text>
  <text class="topic topic-right" x="1222" y="559">Retirement</text>
  <text class="topic topic-right" x="1222" y="681">Dreams &amp; Goals</text>
  <text class="topic topic-right" x="1222" y="763">Health and</text>
  <text class="topic topic-right" x="1222" y="794">Wellbeing</text>

  <!-- Left icons -->
  <path class="icon" d="M105,352 C80,335 78,318 84,311 C92,302 103,306 105,314 C107,306 118,302 126,311 C132,318 130,335 105,352 Z M100,354 L110,350 M100,350 L110,354"/>
  <g class="icon">
    <path d="M75,437 L105,416 L135,437 M81,432 V463 H129 V432 M74,463 H136"/>
    <path d="M119,423 V416 H126 V428"/>
    <rect x="88" y="444" width="10" height="19"/>
    <rect x="107" y="444" width="13" height="8"/>
    <line x1="86" y1="456" x2="100" y2="456"/>
  </g>
  <g class="icon">
    <circle cx="105" cy="551" r="14"/>
    <line x1="105" y1="565" x2="105" y2="584"/>
    <path d="M88,589 V576 H103 V589 M107,589 V576 H121 V589 M79,589 H131"/>
  </g>
  <text class="icon-text" x="105" y="558">$</text>
  <g class="icon">
    <circle cx="105" cy="695" r="23"/>
    <ellipse cx="105" cy="695" rx="10" ry="23"/>
    <line x1="82" y1="695" x2="128" y2="695"/>
    <line x1="86" y1="684" x2="124" y2="684"/>
    <line x1="86" y1="706" x2="124" y2="706"/>
    <line x1="105" y1="672" x2="105" y2="718"/>
  </g>
  <g class="icon">
    <path d="M83,788 H110 L118,796 V836 H83 Z"/>
    <path d="M88,797 H104 M88,804 H108 M88,811 H100 M88,818 H98"/>
    <path d="M126,800 L131,805 L111,829 L104,832 L106,825 Z"/>
  </g>

  <!-- Right icons -->
  <g class="icon">
    <path d="M1260,317 V309 Q1260,304 1265,304 H1289 Q1294,304 1294,309 V317"/>
    <path d="M1254,344 V325 Q1254,319 1260,319 Q1266,319 1266,325 V344 Z M1288,344 V325 Q1288,319 1294,319 Q1300,319 1300,325 V344 Z"/>
    <path d="M1266,333 H1288"/>
  </g>
  <g class="icon">
    <ellipse cx="1268" cy="428" rx="14" ry="4"/>
    <path d="M1254,428 V456 M1282,428 V448 M1254,435 Q1268,441 1282,435 M1254,442 Q1268,448 1282,442 M1254,449 Q1262,453 1270,452 M1254,456 Q1260,459 1270,459"/>
    <ellipse cx="1285" cy="452" rx="14" ry="4"/>
    <path d="M1271,452 V466 Q1285,472 1299,466 V452 M1271,459 Q1285,465 1299,459"/>
  </g>
  <g class="icon">
    <circle cx="1277" cy="543" r="7"/>
    <path d="M1277,530 V533 M1277,553 V556 M1264,543 H1267 M1287,543 H1290 M1268,534 L1270,536 M1284,550 L1286,552 M1268,552 L1270,550 M1284,536 L1286,534"/>
    <path d="M1250,585 L1274,563 L1289,576 L1297,569 L1304,585 Z"/>
  </g>
  <g class="icon">
    <path d="M1297,676 A22,22 0 1 0 1297,712 A18,18 0 1 1 1297,676 Z"/>
    <path d="M1287,679 L1290,686 L1297,686 L1291,691 L1293,698 L1287,694 L1281,698 L1283,691 L1277,686 L1284,686 Z"/>
  </g>
  <g class="icon">
    <circle cx="1260" cy="802" r="6"/>
    <path d="M1260,808 V822 Q1260,834 1271,834 Q1280,834 1280,822 V814"/>
    <path d="M1270,790 Q1266,790 1266,800 Q1266,814 1280,814 Q1294,814 1294,800 Q1294,790 1290,790"/>
    <circle cx="1270" cy="788" r="1.5"/>
    <circle cx="1290" cy="788" r="1.5"/>
  </g>

  <!-- Licence -->
  <text class="licence" x="689" y="932">Tellora Counsel Pty Ltd (538216) is an Authorised Representative of Brindle Estate Capital Group Pty Ltd AFSL No: 613985 ABN 57 218 964 402</text>
</svg>
</div>
</body>
</html>
```